Swimming Pool Business Billboard

10' x 24' Billboard displaying company name, logo and phone number. Picture of swimming pool activity; kids playing , swimming, etc. Bullet points possibly shown: New Construction, Repairs, Weekly maintenance.

Industry/Entity Type

Swimming pool construction, repairs and maintenance.

Font styles to use
Sans Serif

Colors
0054AA
0677BA
7BADD7
CADEEF
E8F1F8

Requirements
Must have
• Rusty & Calder Pembrook, RUSTY'S POOLS & Service,
Nice to have
• Prefer to have my last name "Pembrook" above the word "POOLS" only in smaller print so that "RUSTYS POOLS" is distinguished.

```html
<!DOCTYPE html>
<html lang="en">
<head>
<meta charset="utf-8">
<title>Rusty's Pools &amp; Service Billboard</title>
<link href="https://fonts.googleapis.com/css2?family=Poppins:wght@500;600;700;800&display=swap" rel="stylesheet">
<style>
  :root {
    --navy: #15426f;
    --sky: #aecde9;
    --white: #ffffff;
    --stage: #8f959d;
    --pool-deep: #1f4fa6;
    --pool-mid: #2e6cc4;
    --pool-light: #a9cfe0;
  }
  * { margin: 0; padding: 0; box-sizing: border-box; }
  html, body { width: 1200px; height: 1200px; overflow: hidden; background: var(--stage); }
  body { position: relative; font-family: "Poppins", sans-serif; color: var(--navy); }

  .billboard {
    position: absolute; left: 104px; top: 393px;
    width: 1598px; height: 666px;
    transform: scale(0.6214); transform-origin: 0 0;
    background: var(--white); overflow: hidden;
    box-shadow: 0 4px 10px rgba(0,0,0,.35);
  }
  .billboard-art { position: absolute; inset: 0; }

  .brand-mark {
    position: absolute; left: 630px; top: 60px; width: 150px;
    display: flex; flex-direction: column; align-items: center; gap: 10px;
    font-weight: 700; font-size: 22px; text-align: center; line-height: 1.1;
  }
  .brand-mark .dot { width: 70px; height: 70px; border-radius: 50%; background: var(--navy); }

  .owners {
    position: absolute; left: 813px; top: 38px; width: 694px; height: 80px;
    background: var(--sky); border-radius: 40px;
    display: flex; align-items: center; justify-content: center;
    font-weight: 700; font-size: 48px; white-space: nowrap;
  }
  .company {
    position: absolute; left: 760px; top: 128px; width: 800px; text-align: center;
    font-weight: 800; line-height: 1; white-space: nowrap;
  }
  .company .name { font-size: 86px; display: block; }
  .company .sub { font-size: 80px; display: block; margin-top: 4px; }

  .services {
    position: absolute; left: 770px; top: 326px; width: 780px; height: 120px;
    display: flex; align-items: flex-start;
  }
  .service {
    display: flex; flex-direction: column; align-items: center; gap: 6px;
    font-weight: 500; font-size: 34px; line-height: 1.2; text-align: center;
  }
  .service.new { width: 290px; }
  .service.repairs { width: 210px; }
  .service.weekly { width: 280px; }
  .service.repairs .label { margin-top: 20px; }
  .tick { width: 24px; height: 24px; }
  .divider { position: absolute; top: 38px; width: 2px; height: 76px; background: #9aa7b5; }

  .phone {
    position: absolute; left: 806px; top: 483px; width: 676px; height: 95px;
    background: var(--navy); border-radius: 48px;
    display: flex; align-items: center; gap: 20px; padding-left: 8px;
    color: var(--white); font-weight: 700; font-size: 72px; letter-spacing: -1px;
    white-space: nowrap;
  }
  .phone-number { line-height: 1; padding-top: 6px; }
  .phone-icon {
    width: 80px; height: 80px; border-radius: 50%;
    background: var(--white); border: 6px solid var(--navy);
    outline: 4px solid var(--white);
    display: flex; align-items: center; justify-content: center; flex: none;
  }

  .contact {
    position: absolute; top: 608px; font-weight: 500; font-size: 26px;
    display: flex; align-items: center; gap: 8px; white-space: nowrap;
  }
  .contact.address { left: 646px; }
  .contact.email { left: 1230px; }
</style>
</head>
<body>
  <div class="billboard">
    <svg class="billboard-art" viewBox="0 0 1598 666" width="1598" height="666">
      <defs>
        <linearGradient id="poolMain" x1="0" y1="0" x2="0" y2="1">
          <stop offset="0" stop-color="#7fae6a"/>
          <stop offset="0.08" stop-color="var(--pool-mid)"/>
          <stop offset="0.7" stop-color="var(--pool-deep)"/>
          <stop offset="1" stop-color="#c9d4d6"/>
        </linearGradient>
        <radialGradient id="poolShallow" cx="0.5" cy="0.45" r="0.6">
          <stop offset="0" stop-color="#d8edf3"/>
          <stop offset="1" stop-color="var(--pool-light)"/>
        </radialGradient>
        <radialGradient id="poolStairs" cx="0.5" cy="0.4" r="0.6">
          <stop offset="0" stop-color="#4a78c8"/>
          <stop offset="1" stop-color="#1c3f95"/>
        </radialGradient>
      </defs>
      <rect class="footer-band" x="0" y="530" width="1598" height="136" fill="var(--sky)"/>
      <circle cx="200" cy="250" r="400" fill="url(#poolMain)" stroke="var(--navy)" stroke-width="8" role="img" aria-label="Photo of a backyard in-ground swimming pool with clear blue water"/>
      <circle cx="588" cy="313" r="106" fill="url(#poolShallow)" stroke="var(--navy)" stroke-width="10" role="img" aria-label="Photo of clear shallow pool water"/>
      <circle cx="463" cy="501" r="146" fill="url(#poolStairs)" stroke="var(--navy)" stroke-width="10" role="img" aria-label="Photo of a pool corner with white entry steps"/>
    </svg>

    <div class="brand-mark"><span class="dot"></span>RUSTY'S POOLS</div>

    <div class="owners">Rusty &amp; Calder Pembrook</div>
    <h1 class="company">
      <span class="name">RUSTY'S POOLS</span>
      <span class="sub">&amp; Service</span>
    </h1>

    <div class="services">
      <div class="service new">
        <svg class="tick" viewBox="0 0 24 24"><circle cx="12" cy="12" r="12" fill="var(--navy)"/><path d="M6.5 12.5l3.5 3.5 7-7.5" fill="none" stroke="#fff" stroke-width="2.6" stroke-linecap="round" stroke-linejoin="round"/></svg>
        <span class="label">New<br>Construction</span>
      </div>
      <div class="service repairs">
        <svg class="tick" viewBox="0 0 24 24"><circle cx="12" cy="12" r="12" fill="var(--navy)"/><path d="M6.5 12.5l3.5 3.5 7-7.5" fill="none" stroke="#fff" stroke-width="2.6" stroke-linecap="round" stroke-linejoin="round"/></svg>
        <span class="label">Repairs</span>
      </div>
      <div class="service weekly">
        <svg class="tick" viewBox="0 0 24 24"><circle cx="12" cy="12" r="12" fill="var(--navy)"/><path d="M6.5 12.5l3.5 3.5 7-7.5" fill="none" stroke="#fff" stroke-width="2.6" stroke-linecap="round" stroke-linejoin="round"/></svg>
        <span class="label">Weekly<br>maintenance</span>
      </div>
      <span class="divider" style="left:286px"></span>
      <span class="divider" style="left:498px"></span>
    </div>

    <div class="phone">
      <span class="phone-icon">
        <svg width="46" height="46" viewBox="0 0 24 24"><path d="M6.6 10.8a15.2 15.2 0 0 0 6.6 6.6l2.2-2.2a1 1 0 0 1 1-.25 11.4 11.4 0 0 0 3.6.57 1 1 0 0 1 1 1V20a1 1 0 0 1-1 1A17 17 0 0 1 3 4a1 1 0 0 1 1-1h3.5a1 1 0 0 1 1 1c0 1.25.2 2.45.57 3.57a1 1 0 0 1-.25 1z" fill="var(--navy)"/></svg>
      </span>
      <span class="phone-number">912-555-0147</span>
    </div>

    <div class="contact address">
      <svg width="18" height="24" viewBox="0 0 18 24"><path d="M9 1a8 8 0 0 0-8 8c0 6 8 14 8 14s8-8 8-14a8 8 0 0 0-8-8z" fill="none" stroke="var(--navy)" stroke-width="2.5"/><circle cx="9" cy="9" r="3" fill="var(--navy)"/></svg>
      2750 Marlow Rd Brantley, GA 31599
    </div>
    <div class="contact email">
      <svg width="24" height="18" viewBox="0 0 24 18"><rect x="1" y="1" width="22" height="16" rx="2" fill="var(--navy)"/><path d="M2 3l10 7 10-7" fill="none" stroke="var(--sky)" stroke-width="2"/></svg>
      rusty@rcpools.net
    </div>
  </div>
</body>
</html>
```